Brevik Fabrication - Business Card Design

We would like a dark (likely black) themed business card to be able to hand out to potential clients. We may list our services on the card or keep it clean. Unsure. Logo attached

```html
<!DOCTYPE html>
<html lang="en">
<head>
<meta charset="utf-8">
<title>Brevik Fabrication – Business Card</title>
<link rel="stylesheet" href="https://fonts.googleapis.com/css2?family=Oswald:wght@500;600&family=Open+Sans:wght@400&display=swap">
<style>
  :root {
    --stage: #141414;
    --card: #222224;
    --card-edge: #2c2c2f;
    --orange: #e0622a;
    --blue: #2f7fcf;
  }
  html, body {
    margin: 0;
    width: 1200px;
    height: 900px;
    overflow: hidden;
    background: var(--stage);
  }
  .canvas {
    position: relative;
    width: 1200px;
    height: 900px;
  }
  .card {
    position: absolute;
    left: 320px;
    width: 560px;
    height: 320px;
    background: var(--card);
    border: 1px solid var(--card-edge);
    border-radius: 18px;
    overflow: hidden;
    box-shadow: 0 12px 30px rgba(0,0,0,.5);
  }
  .card--front { top: 90px; }
  .card--back { top: 480px; }

  /* front */
  .brand {
    position: absolute;
    inset: 0;
    display: flex;
    align-items: center;
    justify-content: center;
    gap: 16px;
  }
  .brand__dot {
    width: 34px;
    height: 34px;
    border-radius: 50%;
    background: var(--orange);
  }
  .brand__name {
    font-family: "Oswald", sans-serif;
    font-weight: 600;
    font-size: 40px;
    letter-spacing: 1px;
    text-transform: uppercase;
    color: var(--blue);
  }

  /* back */
  .card__mark {
    position: absolute;
    left: -70px;
    top: -60px;
    width: 270px;
    height: 270px;
    border-radius: 50%;
    background: var(--orange);
  }
  .contact {
    position: absolute;
    left: 255px;
    top: 62px;
    font-family: "Open Sans", sans-serif;
    color: var(--blue);
  }
  .contact__name {
    margin: 0;
    font-family: "Oswald", sans-serif;
    font-weight: 500;
    font-size: 28px;
    line-height: 1;
    text-transform: uppercase;
  }
  .contact__name .surname { color: var(--orange); }
  .contact__role {
    margin: 6px 0 22px;
    font-family: "Oswald", sans-serif;
    font-weight: 500;
    font-size: 15px;
    letter-spacing: .5px;
    text-transform: uppercase;
  }
  .contact__list {
    list-style: none;
    margin: 0;
    padding: 0;
  }
  .contact__item {
    display: flex;
    align-items: flex-start;
    gap: 12px;
    font-size: 14px;
    line-height: 18px;
    margin-bottom: 10px;
  }
  .contact__icon {
    flex: none;
    width: 18px;
    height: 18px;
  }
</style>
</head>
<body>
<main class="canvas">
  <section class="card card--front" aria-label="Card front">
    <div class="brand">
      <span class="brand__dot"></span>
      <span class="brand__name">Brevik Fabrication Inc</span>
    </div>
  </section>

  <section class="card card--back" aria-label="Card back">
    <div class="card__mark" role="img" aria-label="Company emblem area"></div>
    <div class="contact">
      <h1 class="contact__name">Daniel <span class="surname">Oakes</span></h1>
      <p class="contact__role">General Manager</p>
      <ul class="contact__list">
        <li class="contact__item">
          <svg class="contact__icon" viewBox="0 0 18 18"><circle cx="9" cy="9" r="8" fill="none" stroke="#e0622a" stroke-width="1.3"/><path d="M6 5.5c.6-.5 1.1-.3 1.4.3l.5 1c.2.5 0 .8-.4 1.1.4.9 1.1 1.6 2 2 .3-.4.6-.6 1.1-.4l1 .5c.6.3.8.8.3 1.4-.9 1-2.4.8-3.9-.6S5 6.4 6 5.5z" fill="#e0622a"/></svg>
          <span>403-555-0172</span>
        </li>
        <li class="contact__item">
          <svg class="contact__icon" viewBox="0 0 18 18"><circle cx="9" cy="9" r="8" fill="none" stroke="#e0622a" stroke-width="1.3"/><rect x="5" y="6" width="8" height="6" rx="1" fill="#e0622a"/><path d="M5.3 6.4 9 9.3l3.7-2.9" fill="none" stroke="#222224" stroke-width="1"/></svg>
          <span>info@brevikfabrication.com</span>
        </li>
        <li class="contact__item">
          <svg class="contact__icon" viewBox="0 0 18 18"><circle cx="9" cy="9" r="8" fill="none" stroke="#e0622a" stroke-width="1.3"/><circle cx="9" cy="9" r="4" fill="none" stroke="#e0622a" stroke-width="1.1"/><path d="M5 9h8M9 5c-1.5 2.5-1.5 5.5 0 8M9 5c1.5 2.5 1.5 5.5 0 8" fill="none" stroke="#e0622a" stroke-width=".8"/></svg>
          <span>www.brevikfabrication.com</span>
        </li>
        <li class="contact__item">
          <svg class="contact__icon" viewBox="0 0 18 18"><circle cx="9" cy="9" r="8" fill="none" stroke="#e0622a" stroke-width="1.3"/><path d="M9 4.5a3 3 0 0 1 3 3c0 2.2-3 5.8-3 5.8S6 9.7 6 7.5a3 3 0 0 1 3-3z" fill="#e0622a"/><circle cx="9" cy="7.5" r="1.1" fill="#222224"/></svg>
          <span>1187 Harlow Rd SE, Calgary<br>AB T2X 4K8 Canada</span>
        </li>
      </ul>
    </div>
  </section>
</main>
</body>
</html>
```